Awesome new dental practice requires a New Letterhead design

We would like a new letterhead design to align with our new business branding & business cards. I have uploaded all the logos & current business card details that can be used. The new website can be viewed here https://lumaveo.com.au

Other useful details: Font Poppins
Colour Palettes:
Dark Pink #c45389
Light Pink: #e83e8c
Black

Please let me know if you have any questions or require anything else.

Industry/Entity Type

Dental

Font styles to use
Other font styles liked:
• Poppins

```html
<!DOCTYPE html>
<html lang="en">
<head>
<meta charset="utf-8">
<title>Lumaveo Letterhead</title>
<link rel="stylesheet" href="https://fonts.googleapis.com/css2?family=Poppins:wght@400;500;600&family=Open+Sans:wght@400;600&family=Mrs+Saint+Delafield&display=swap">
<style>
  :root {
    --backdrop: #b2b2b2;
    --paper: #fafafa;
    --ink: #1a1a1a;
    --body-text: #6a6a6a;
    --pink: #c45389;
    --signature-blue: #1f7fc0;
  }
  * { margin: 0; padding: 0; box-sizing: border-box; }
  html, body { width: 1200px; height: 1001px; overflow: hidden; }
  body { background: var(--backdrop); position: relative; }
  .letterhead {
    position: absolute; left: 287px; top: 58px;
    width: 625px; height: 884px;
    background: var(--paper);
    font-family: "Open Sans", Arial, sans-serif;
    color: var(--body-text);
  }
  .brand { position: absolute; left: 62px; top: 64px; }
  .brand-name {
    font-family: "Poppins", Arial, sans-serif;
    font-weight: 500; font-size: 34px; line-height: 1;
    color: var(--ink); letter-spacing: 0.2px;
  }
  .brand-tagline {
    margin-top: 8px;
    font-family: "Poppins", Arial, sans-serif;
    font-weight: 600; font-size: 10.2px; letter-spacing: 2.1px;
    color: var(--ink);
  }
  .header-rule { position: absolute; left: 0; top: 0; }
  .contact {
    position: absolute; right: 68px; top: 56px;
    font-family: "Poppins", Arial, sans-serif; font-size: 11px;
    color: var(--ink); text-align: right; list-style: none;
  }
  .contact li { display: flex; justify-content: flex-end; align-items: center; gap: 7px; height: 14.5px; }
  .contact svg { width: 9px; height: 9px; fill: var(--pink); }
  .address {
    position: absolute; right: 62px; top: 108px;
    font-family: "Poppins", Arial, sans-serif; font-size: 11px;
    line-height: 15px; color: var(--ink); text-align: right; font-style: normal;
  }
  .letter-body {
    position: absolute; left: 59px; width: 507px;
    font-size: 9.8px; line-height: 16px; letter-spacing: -0.15px;
  }
  .salutation { top: 210px; }
  .paragraph { text-align: justify; }
  .p1 { top: 258px; } .p2 { top: 369px; } .p3 { top: 480px; }
  .sign-off { position: absolute; left: 59px; top: 593px; }
  .sign-name { font-weight: 600; font-size: 9.8px; color: #555; }
  .signature {
    font-family: "Mrs Saint Delafield", cursive;
    font-size: 34px; color: var(--signature-blue); line-height: 1; margin-top: 12px;
  }
  .sign-role { font-size: 9.8px; margin-top: 4px; }
  .motto-line {
    position: absolute; top: 838px; left: 0; width: 625px;
    display: flex; justify-content: center; align-items: center; gap: 10px;
    font-family: "Poppins", Arial, sans-serif; font-weight: 500; font-size: 12.3px; color: var(--ink);
  }
  .motto-line .accent { color: var(--pink); }
  .motto-line .dash { width: 47px; height: 1.5px; background: var(--pink); }
</style>
</head>
<body>
  <main class="letterhead">
    <div class="brand">
      <div class="brand-name">lumaveo</div>
      <div class="brand-tagline">DENTISTRY &amp; ORTHODONTICS</div>
    </div>

    <svg class="header-rule" width="625" height="200" viewBox="0 0 625 200" aria-hidden="true">
      <path d="M59 132 H302 C330 132 330 105 362 105 H566" fill="none" stroke="var(--pink)" stroke-width="1.1"/>
    </svg>

    <ul class="contact">
      <li>(08) 9000 4821
        <svg viewBox="0 0 10 10"><path d="M1 3.5 C1 2 3 1 5 1 C7 1 9 2 9 3.5 L7.3 4.2 L6.8 3 H3.2 L2.7 4.2 Z M2.5 5 H7.5 L8.5 9 H1.5 Z"/></svg>
      </li>
      <li>hello@lumaveo.com.au
        <svg viewBox="0 0 10 10"><path d="M0.5 2 H9.5 V8 H0.5 Z M1.3 2.6 L5 5.5 L8.7 2.6" stroke="#fff" stroke-width="0.6"/></svg>
      </li>
      <li>www.lumaveo.com.au
        <svg viewBox="0 0 10 10"><circle cx="5" cy="5" r="4.5"/><path d="M0.5 5 H9.5 M5 0.5 V9.5 M2 2.5 H8 M2 7.5 H8" stroke="#fff" stroke-width="0.5" fill="none"/></svg>
      </li>
    </ul>

    <address class="address">Unit 9, 27 Marlow Street<br>Seabrook WA 6930</address>

    <p class="letter-body salutation">Dear Sir,</p>

    <p class="letter-body paragraph p1">Lorem Ipsum is simply dummy text of the printing and typesetting industry. Lorem Ipsum has been the industry's standard dummy text ever since the 1500s, when an unknown printer took a galley of type and scrambled it to make a type specimen book. It has survived not only five centuries, but also the leap into electronic typesetting, remaining essentially unchanged. It was popularised in the 1960s with the release of transfer sheets containing Lorem Ipsum passages, and more recently with desktop publishing software like layout programs including versions of Lorem Ipsum.</p>

    <p class="letter-body paragraph p2">Lorem Ipsum is simply dummy text of the printing and typesetting industry. Lorem Ipsum has been the industry's standard dummy text ever since the 1500s, when an unknown printer took a galley of type and scrambled it to make a type specimen book. It has survived not only five centuries, but also the leap into electronic typesetting, remaining essentially unchanged. It was popularised in the 1960s with the release of transfer sheets containing Lorem Ipsum passages, and more recently with desktop publishing software like layout programs including versions of Lorem Ipsum.</p>

    <p class="letter-body paragraph p3">Lorem Ipsum is simply dummy text of the printing and typesetting industry. Lorem Ipsum has been the industry's standard dummy text ever since the 1500s, when an unknown printer took a galley of type and scrambled it to make a type specimen book.</p>

    <div class="sign-off">
      <div class="sign-name">Your Name</div>
      <div class="signature">Daniel Corvell</div>
      <div class="sign-role">CEO &nbsp;|&nbsp; Owner</div>
    </div>

    <div class="motto-line">
      <span class="dash"></span>
      <span>Life is short. <span class="accent">Smile</span> while you still have teeth.</span>
      <span class="dash"></span>
    </div>
  </main>
</body>
</html>
```